Metal Warranty card design for Wristwatch brand

I will need a design for a warranty card that will be included with all of our watches. This card will be made from metal and will be rose gold plated. I have attached an example of our current card.

Website with our watch designs: www.quarnitimepieces.com

Target Market(s)

Men, 20-40s, watch collectors

Requirements
Must have
• Requires these fields and text (follow the example):
• Front:
• www.quarnitimepieces.com
• Back:
• 1 Year Limited Warranty
• Serial: (signature panel)
• Date: (Signature panel)
• Seller: (large panel)
Nice to have
• Cut outs, watch themed

```html
<!DOCTYPE html>
<html lang="en">
<head>
<meta charset="utf-8">
<title>Quarni Warranty Card</title>
<link rel="stylesheet" href="https://fonts.googleapis.com/css2?family=Montserrat:wght@300;400;600&display=swap">
<style>
  :root {
    --page-bg: #e9e7e4;
    --card-black: #050505;
    --ink-white: #ffffff;
    --silver-light: #f4f4f4;
    --silver-mid: #bdbdbd;
    --silver-dark: #8a8a8a;
    --text-dark: #1a1a1a;
  }
  * { margin: 0; padding: 0; box-sizing: border-box; }
  html, body {
    width: 1200px;
    height: 831px;
    overflow: hidden;
    background: var(--page-bg);
    font-family: "Montserrat", sans-serif;
  }
  .canvas {
    position: relative;
    width: 1200px;
    height: 831px;
  }
  .card {
    position: absolute;
    top: 265px;
    width: 525px;
    height: 300px;
    background: var(--card-black);
    border-radius: 6px;
    overflow: hidden;
    box-shadow: 0 10px 28px rgba(0,0,0,0.25);
  }
  .card--back { left: 50px; }
  .card--front { left: 625px; }

  /* Back of card */
  .warranty-title {
    position: absolute;
    top: 24px;
    left: 40px;
    color: var(--ink-white);
    font-weight: 300;
    font-size: 19px;
    letter-spacing: 1px;
  }
  .warranty-fields {
    position: absolute;
    top: 66px;
    left: 28px;
  }
  .field {
    display: flex;
    align-items: flex-start;
    margin-bottom: 8px;
  }
  .field-label {
    width: 82px;
    color: var(--ink-white);
    font-weight: 300;
    font-size: 17px;
    letter-spacing: 0.5px;
    line-height: 20px;
  }
  .field-panel {
    background: var(--ink-white);
  }
  .field-panel--line { width: 145px; height: 18px; margin-top: 6px; }
  .field-panel--large { width: 170px; height: 92px; margin-top: 6px; }

  .brand {
    position: absolute;
    display: flex;
    flex-direction: column;
    align-items: center;
    color: var(--ink-white);
  }
  .brand-circle {
    border: 2px solid currentColor;
    border-radius: 50%;
  }
  .brand-name {
    font-weight: 300;
    letter-spacing: 3px;
    line-height: 1;
  }
  .card--back .brand { right: 42px; bottom: 52px; }
  .card--back .brand-circle { width: 56px; height: 56px; margin-bottom: 14px; }
  .card--back .brand-name { font-size: 40px; }

  /* Front of card */
  .card--front .brand { left: 205px; top: 38px; color: var(--silver-mid); }
  .card--front .brand-circle { width: 74px; height: 74px; margin-bottom: 16px; border-width: 3px; }
  .card--front .brand-name { font-size: 52px; }

  .front-swoosh {
    position: absolute;
    inset: 0;
    width: 525px;
    height: 300px;
  }
  .site-url {
    font-family: "Montserrat", sans-serif;
    font-weight: 600;
    font-size: 15px;
    letter-spacing: 4px;
    fill: var(--text-dark);
  }
</style>
</head>
<body>
<main class="canvas">

  <section class="card card--back" aria-label="Warranty card back">
    <h2 class="warranty-title">1 YEAR LIMITED WARRANTY</h2>
    <div class="warranty-fields">
      <div class="field">
        <span class="field-label">SERIAL</span>
        <span class="field-panel field-panel--line"></span>
      </div>
      <div class="field">
        <span class="field-label">DATE</span>
        <span class="field-panel field-panel--line"></span>
      </div>
      <div class="field">
        <span class="field-label">SELLER</span>
        <span class="field-panel field-panel--large"></span>
      </div>
    </div>
    <div class="brand">
      <span class="brand-circle"></span>
      <span class="brand-name">QUARNI</span>
    </div>
  </section>

  <section class="card card--front" aria-label="Warranty card front">
    <svg class="front-swoosh" viewBox="0 0 525 300" aria-hidden="false">
      <defs>
        <linearGradient id="silverBand" x1="0" y1="0" x2="1" y2="1">
          <stop offset="0" stop-color="#9a9a9a"/>
          <stop offset="0.35" stop-color="#f6f6f6"/>
          <stop offset="0.7" stop-color="#cfcfcf"/>
          <stop offset="1" stop-color="#8f8f8f"/>
        </linearGradient>
        <path id="urlCurve" d="M40,212 Q250,232 470,306"/>
      </defs>
      <path d="M0,170 Q230,182 525,262 L525,300 L0,300 Z" fill="url(#silverBand)"/>
      <path d="M0,186 Q230,198 525,278" fill="none" stroke="#050505" stroke-width="3"/>
      <text class="site-url"><textPath href="#urlCurve">www.quarnitimepieces.com</textPath></text>
    </svg>
    <div class="brand">
      <span class="brand-circle"></span>
      <span class="brand-name">QUARNI</span>
    </div>
  </section>

</main>
</body>
</html>
```